依頼詳細
【Tobiraのサービス特徴はこの3つ!】
●無料で請求書管理
請求書の作成・PDFダウンロードなどの機能はずっと無料でご利用になれます。顧客の数や、請求書の枚数に制限はありません。さらに有料プランなら見積り機能も使えます
●あんしんの印刷・郵送システム
Tobiraでは安全なドキュメントセンターで印刷、封入、封かん、発送を行なっています。それぞれの作業は機械が行うため請求書をの中身を人が見るということや人為的なミスはありません。詳しくはこちら
●どこでも請求書の作成・管理ができる
専用画面からログインすれば、書き方がわからなくてもテンプレートの必要事項を埋めるだけで出張先や自宅、iPad、スマートフォンなどからいつでも作成・編集できます。

---------------------------------------------------------------------------------

今回は、2種類のデザインを採用させていただきます。
1件10万円で、2種類の募集となりますので、
ドド~ンと総額20万円のキャンペーンとなります。
記載項目
■ 希望するデザイン
フリーランスのエンジニアさん、デザイナーさんが使いたくなる、オシャレで格好いい請求書の、オリジナルのデザインをご提案ください。

また、以下内容は請求書面として必要な事項となりますので必ず記載ください。
(現状の請求書のデータをアップロードしておりますので参照・活用ください)
・請求年月日
・請求先名称
・請求元(名前、住所、TEL、FAX、メールアドレス)
・請求元印影画像
・請求金額合計
・請求明細(20行、小計、消費税、合計金額)
・備考欄(3行)
・振込口座欄(1行)
希望イメージ
• +5 0 +5
• シンプル
複雑
• 単色
カラフル
• 暗い
明るい
• 日常
高級
• 遊び心
厳粛
• 未来的
伝統的
• 女性的
男性的
希望する色
色の指定はございません
納品ファイル
• イラストレーター形式 (.ai)
• フォトショップ形式 (.psd)
補足説明
■ 納品ファイルの希望
Illustrator形式、Photoshop形式、Fireworks形式
(最大容量は1024kbとしてそれ以下で作ってください)
依頼公開後の追記内容
■ 選んだ理由

bluewhistlerさんの作品は、どの業種でも使いやすく受け取り手も安心できるデザインということで選ばせて頂きました

もう一点は(http://www.kumoshi-hub.jp/work/proposal/5830417)になります。(現在システムの都合で当選にできていません)
k-atelierさんの作品は請求書のかっちりした感じに少し遊びを加えた感じのバランスがよく、採用しました。

■ 提案者全員のお礼・コメント

これほど多くの応募をいただけるとは思っておらずとても驚くとともに、感謝の気持でいっぱいです。

請求書のデザインということで、単純にデザイン性だけでは判断できず、どれも素敵な作品ばかりだったので選定には本当に時間がかかりました。

今回の当選作品以外にもTobira賞として10点ほど買取のオファーを出させて頂きます。どうぞよろしくおねがいします。

この度は本当にご応募ありがとうございました。

```html
<!DOCTYPE html>
<html lang="ja">
<head>
<meta charset="utf-8">
<title>請求書 INVOICE</title>
<link href="https://fonts.googleapis.com/css2?family=Noto+Sans+JP:wght@300;400;500;700&display=swap" rel="stylesheet">
<style>
  :root{
    --paper:#ffffff;
    --ink:#333333;
    --ink-soft:#777777;
    --rule:#9a9a9a;
    --band-dark:#6e6e6e;
    --band-mid:#d9d9d9;
    --row-alt:#efefef;
    --seal:#c9515c;
  }
  *{box-sizing:border-box;margin:0;padding:0}
  html,body{width:849px;height:1200px;overflow:hidden}
  body{background:var(--paper);color:var(--ink);font-family:"Noto Sans JP",sans-serif;position:relative}
  .abs{position:absolute}

  .issue-meta{right:127px;top:28px;text-align:right;font-size:12px;line-height:20px;color:var(--ink)}
  .issue-meta .label{color:var(--ink-soft);font-size:9px;margin-right:6px}

  .doc-title{left:0;right:0;top:56px;text-align:center;font-size:30px;font-weight:500;letter-spacing:14px;padding-left:14px}
  .doc-subtitle{left:0;right:0;top:106px;text-align:center;font-size:9px;letter-spacing:3px;color:var(--ink-soft)}
  .title-rule{left:127px;right:127px;top:124px;height:1px;background:var(--rule)}

  .client{left:127px;top:190px;width:283px;border-bottom:1px solid var(--ink);padding-bottom:6px;font-size:19px;font-weight:500;display:flex;justify-content:space-between;align-items:flex-end}
  .client .honorific{font-size:12px;font-weight:400}
  .lead{left:127px;top:236px;font-size:9px;color:var(--ink-soft)}

  .amount-due{left:127px;top:260px;width:283px;height:32px;display:flex;align-items:center;border-bottom:1px solid var(--ink)}
  .amount-due .label{background:var(--band-mid);height:100%;width:150px;display:flex;align-items:center;padding-left:10px;font-size:12px}
  .amount-due .value{padding-left:18px;font-size:22px;font-weight:300;letter-spacing:1px}

  .issuer{left:487px;top:190px;font-size:10px;line-height:17px}
  .issuer .name{font-size:12px;font-weight:500;margin-bottom:4px}
  .seal{left:676px;top:198px;width:112px;height:112px;border-radius:14px;background:var(--seal);opacity:.85}

  .items{left:127px;top:348px;width:595px;border-collapse:collapse;font-size:11px}
  .items th{background:var(--band-dark);color:#fff;font-weight:400;font-size:9px;height:17px;letter-spacing:4px}
  .items td{height:20.4px;border-bottom:1px solid #e2e2e2;padding:0 8px}
  .items tbody tr:nth-child(even) td{background:var(--row-alt)}
  .items td.num{text-align:right}
  .items td.qty{text-align:center}
  .items td+td{border-left:1px solid #d0d0d0}
  .items tbody{border-bottom:1px solid var(--rule)}

  .notes{left:127px;top:838px;width:368px;height:110px;border:1px solid var(--rule)}
  .notes .head{height:18px;background:var(--row-alt);font-size:9px;padding-left:8px;line-height:18px}
  .notes .line{height:30px;border-bottom:1px dotted #cfcfcf;margin:0 8px}

  .totals{left:510px;top:828px;width:212px;border-collapse:collapse;font-size:11px}
  .totals td{height:34px;border-bottom:1px solid #cfcfcf;padding:0 8px}
  .totals td.label{font-size:9px;background:var(--row-alt);width:98px}
  .totals td.num{text-align:right}
  .totals tr.grand td{border-bottom:1px solid var(--ink)}

  .bank-band{left:127px;top:982px;width:595px;height:14px;background:var(--band-dark);color:#fff;font-size:8px;line-height:14px;padding-left:8px;letter-spacing:2px}
  .bank{left:127px;top:998px;width:595px;height:26px;border-bottom:1px solid var(--rule);font-size:11px;line-height:26px;padding-left:8px;word-spacing:6px}
</style>
</head>
<body>
  <div class="abs issue-meta">
    <div>2013 年 05 月 11 日</div>
    <div><span class="label">請求番号</span>20130511-005</div>
  </div>

  <h1 class="abs doc-title">請求書</h1>
  <div class="abs doc-subtitle">INVOICE</div>
  <div class="abs title-rule"></div>

  <div class="abs client"><span>サンプル株式会社</span><span class="honorific">様</span></div>
  <p class="abs lead">下記のとおりご請求申し上げます。</p>
  <div class="abs amount-due"><span class="label">ご請求金額</span><span class="value">¥ 84,000 -</span></div>

  <address class="abs issuer" style="font-style:normal">
    <div class="name">ミナトワークス株式会社</div>
    <div>〒460-0012 愛知県名古屋市中区</div>
    <div>栄町2丁目8-3 さくらビル5F</div>
    <div>TEL 052-555-0142</div>
    <div>FAX 052-555-0143</div>
    <div>info@minatoworks.jp</div>
  </address>
  <div class="abs seal" role="img" aria-label="請求元の社印（朱色の角印）"></div>

  <table class="abs items">
    <colgroup><col style="width:326px"><col style="width:57px"><col style="width:98px"><col style="width:114px"></colgroup>
    <thead><tr><th>品番・品名</th><th>数量</th><th>単価</th><th>金額</th></tr></thead>
    <tbody>
      <tr><td>デザイン</td><td class="qty">1</td><td class="num">20,000</td><td class="num">20,000</td></tr>
      <tr><td>企画・制作費用</td><td class="qty">1</td><td class="num">60,000</td><td class="num">60,000</td></tr>
      <tr><td></td><td></td><td></td><td></td></tr><tr><td></td><td></td><td></td><td></td></tr>
      <tr><td></td><td></td><td></td><td></td></tr><tr><td></td><td></td><td></td><td></td></tr>
      <tr><td></td><td></td><td></td><td></td></tr><tr><td></td><td></td><td></td><td></td></tr>
      <tr><td></td><td></td><td></td><td></td></tr><tr><td></td><td></td><td></td><td></td></tr>
      <tr><td></td><td></td><td></td><td></td></tr><tr><td></td><td></td><td></td><td></td></tr>
      <tr><td></td><td></td><td></td><td></td></tr><tr><td></td><td></td><td></td><td></td></tr>
      <tr><td></td><td></td><td></td><td></td></tr><tr><td></td><td></td><td></td><td></td></tr>
      <tr><td></td><td></td><td></td><td></td></tr><tr><td></td><td></td><td></td><td></td></tr>
      <tr><td></td><td></td><td></td><td></td></tr><tr><td></td><td></td><td></td><td></td></tr>
    </tbody>
  </table>

  <div class="abs notes">
    <div class="head">備考</div>
    <div class="line"></div><div class="line"></div><div class="line" style="border-bottom:none"></div>
  </div>

  <table class="abs totals">
    <tr><td class="label">小計</td><td class="num">80,000</td></tr>
    <tr><td class="label">消費税（5%）</td><td class="num">4,000</td></tr>
    <tr class="grand"><td class="label">合計金額</td><td class="num">84,000</td></tr>
  </table>

  <div class="abs bank-band">お振込先</div>
  <div class="abs bank">日本ジャパン銀行 中央支店 普通口座 01234567 サンプル太郎</div>
</body>
</html>
```